Pelican Crest landing page design

We need a landing page designed for an ecommerce website that sales fresh US domestic shrimp from the Gulf of Mexico and ships them direct to the consumer "From Our Shore To Your Door". For the landing page, we would like customers to be able to place an order and or inquire further about our product as well as links to social media. The company logo is attached

1 page

```html
<!DOCTYPE html>
<html lang="en">
<head>
<meta charset="utf-8">
<title>Pelican Crest — Wild Gulf Shrimp</title>
<link href="https://fonts.googleapis.com/css2?family=Poppins:wght@300;400;500;600;700&display=swap" rel="stylesheet">
<style>
:root{
  --sky:#9ab5cc;
  --sky-dark:#86a5bf;
  --coral:#ef7b4f;
  --ink:#2b2b2b;
  --muted:#8a8a8a;
  --line:#e6e6e6;
  --white:#ffffff;
  --dark:#222222;
}
*{margin:0;padding:0;box-sizing:border-box}
html,body{width:694px;height:1200px;overflow:hidden;background:var(--white)}
body{font-family:'Poppins',sans-serif;color:var(--ink);position:relative}
.abs{position:absolute}

.topbar{left:0;top:0;width:694px;height:14px;background:var(--sky);font-size:4.5px;color:var(--white)}
.topbar span{position:absolute;top:4px}

.header{left:0;top:14px;width:694px;height:33px;background:var(--white)}
.brand{left:125px;top:8px;display:flex;align-items:center;gap:4px}
.brand-dot{width:18px;height:18px;border:1px solid var(--ink);border-radius:50%;flex:none}
.brand-name{font-size:7.5px;font-weight:500;letter-spacing:1px;color:var(--ink);text-transform:uppercase;white-space:nowrap}
.nav{left:242px;top:15px;display:flex;gap:0;font-size:5.2px;letter-spacing:.6px;font-weight:500}
.nav a{color:var(--ink);text-decoration:none;position:absolute;white-space:nowrap}
.nav a.active{color:var(--coral)}
.social-dot{width:17px;height:17px;border-radius:50%;background:#efefef;top:8px}
.icon{top:11px}

.hero{left:0;top:47px;width:694px;height:203px;background:radial-gradient(ellipse at 30% 40%,#c77a5c 0%,#a4533e 45%,#6e3a2d 100%)}
.hero-ring{left:476px;top:76px;width:88px;height:88px;border:1px solid rgba(255,255,255,.7);border-radius:50%}
.hero-kicker{left:123px;top:111px;font-size:12.5px;font-weight:300;color:var(--white)}
.hero-title{left:123px;top:130px;font-size:16px;font-weight:600;color:var(--white)}
.btn-shop{left:124px;top:165px;width:62px;height:17px;background:var(--sky);color:var(--white);font-size:4.8px;letter-spacing:.6px;font-weight:500;display:flex;align-items:center;justify-content:center}
.slides{top:234px;font-size:6px;color:var(--white)}
.slide-bar{left:148px;top:242px;width:12px;height:1px;background:var(--white)}

.perk{top:272px;display:flex;gap:8px;align-items:center}
.perk h4{font-size:6px;font-weight:500;text-transform:uppercase}
.perk p{font-size:4.5px;color:var(--muted);margin-top:2px}
.rule{left:144px;top:306px;width:422px;height:1px;background:var(--line)}

.tab{top:334px;font-size:6.5px;letter-spacing:.8px;color:var(--ink);text-transform:uppercase}
.tab.active{color:var(--coral);border-bottom:1px solid var(--coral);padding-bottom:1px}

.card{width:98px;height:110px;border:1px solid var(--coral);background:var(--white)}
.card .shot{position:absolute;left:19px;top:10px;width:60px;height:58px;border-radius:45%}
.card .name{position:absolute;left:0;right:0;top:77px;text-align:center;font-size:6.5px}
.card .price{position:absolute;left:0;right:0;top:86px;text-align:center;font-size:7px}
.card .price s{font-size:5px;color:#bbb;margin-left:2px}
.shot.red{background:radial-gradient(circle,#d4402e 0%,#e2765f 45%,rgba(255,255,255,0) 72%)}
.shot.orange{background:radial-gradient(circle,#f07a45 0%,#f5a37d 45%,rgba(255,255,255,0) 72%)}
.shot.brown{background:radial-gradient(circle,#8a7258 0%,#b5a48f 45%,rgba(255,255,255,0) 72%)}
.shot.trio{background:radial-gradient(ellipse,#e2502f 0%,#f0886a 45%,rgba(255,255,255,0) 72%)}

.hair{top:779px;height:1px;background:var(--line)}
.btn-go{left:316px;top:770px;width:61px;height:19px;border:1px solid var(--sky);font-size:5px;letter-spacing:.6px;font-weight:600;display:flex;align-items:center;justify-content:center;background:var(--white)}

.why{left:0;top:817px;width:694px;height:201px;background:radial-gradient(ellipse at 50% 50%,#8a4f38 0%,#6b3c2c 55%,#4e2d23 100%)}
.why-title{left:0;width:694px;top:852px;text-align:center;font-size:12px;font-weight:600;color:var(--white)}
.why-line{left:332px;top:873px;width:28px;height:1px;background:var(--coral)}
.why-ring{left:308px;top:892px;width:76px;height:76px;border:1px solid rgba(255,255,255,.75);border-radius:50%}
.point{width:110px;color:var(--white)}
.point h5{font-size:6.5px;font-weight:600}
.point p{font-size:5.5px;line-height:8px;color:rgba(255,255,255,.75);margin-top:2px}
.point.left{text-align:right}

.newsletter{left:0;top:1018px;width:694px;height:101px;background:var(--sky)}
.nl-title{left:0;width:694px;top:1036px;text-align:center;font-size:11px;font-weight:300;color:var(--white)}
.nl-sub{left:0;width:694px;top:1056px;text-align:center;font-size:5px;color:var(--white)}
.nl-input{left:243px;top:1073px;width:149px;height:17px;background:var(--white);font-size:5px;color:#bbb;padding:6px 7px}
.nl-btn{left:392px;top:1073px;width:58px;height:17px;background:var(--dark);color:var(--white);font-size:5px;font-weight:600;letter-spacing:.5px;display:flex;align-items:center;justify-content:center}

.pay{top:1141px;width:14px;height:9px;border-radius:1px}
.foot-brand{left:310px;top:1133px;display:flex;align-items:center;gap:4px}
.copy{left:0;width:694px;top:1164px;text-align:center;font-size:5px;color:var(--muted)}
.foot-links{left:274px;top:1178px;font-size:5.2px;color:var(--ink)}
.foot-links span{position:absolute;white-space:nowrap}
</style>
</head>
<body>

<div class="abs topbar">
  <span style="left:450px">English ⌄</span>
  <span style="left:487px">Dollar (US) ⌄</span>
  <span style="left:533px">Register / Sign in</span>
</div>

<header class="abs header">
  <div class="abs brand"><div class="brand-dot"></div><div class="brand-name">Pelican Crest</div></div>
  <nav class="abs nav">
    <a class="active" style="left:0">HOME</a>
    <a style="left:36px">SHOP</a>
    <a style="left:72px">ABOUT US</a>
    <a style="left:117px">PRODUCTS</a>
    <a style="left:163px">CONTACT</a>
  </nav>
  <div class="abs social-dot" style="left:452px"></div>
  <div class="abs social-dot" style="left:473px"></div>
  <div class="abs social-dot" style="left:495px"></div>
  <div class="abs social-dot" style="left:517px"></div>
  <svg class="abs icon" style="left:543px" width="9" height="9" viewBox="0 0 24 24" fill="none" stroke="#2b2b2b" stroke-width="2.4"><path d="M12 21s-8-5-8-11a4.5 4.5 0 0 1 8-2.8A4.5 4.5 0 0 1 20 10c0 6-8 11-8 11z"/></svg>
  <svg class="abs icon" style="left:560px" width="9" height="9" viewBox="0 0 24 24" fill="none" stroke="#2b2b2b" stroke-width="2.4"><path d="M2 3h3l3 12h11l3-9H7"/><circle cx="9" cy="20" r="1.5"/><circle cx="18" cy="20" r="1.5"/></svg>
  <div class="abs" style="left:548px;top:9px;width:4px;height:4px;border-radius:50%;background:var(--coral)"></div>
  <div class="abs" style="left:565px;top:9px;width:4px;height:4px;border-radius:50%;background:var(--coral)"></div>
</header>

<section class="abs hero" role="img" aria-label="Close-up photo of freshly caught wild Gulf shrimp held in hands"></section>
<div class="abs hero-ring"></div>
<div class="abs hero-kicker">We represent the finest</div>
<div class="abs hero-title">Wild Shrimp from the U.S.</div>
<div class="abs btn-shop">SHOP NOW ›</div>
<div class="abs slides" style="left:129px">01</div>
<div class="abs slides" style="left:150px;top:229px">02</div>
<div class="abs slide-bar"></div>
<div class="abs slides" style="left:168px">03</div>

<div class="abs perk" style="left:166px">
  <svg width="14" height="14" viewBox="0 0 24 24" fill="none" stroke="#ef7b4f" stroke-width="1.6"><circle cx="12" cy="8" r="5"/><path d="M2 20h6l6-3h6"/></svg>
  <div><h4>Free Delivery</h4><p>For all order over 99$</p></div>
</div>
<div class="abs perk" style="left:303px">
  <svg width="15" height="14" viewBox="0 0 24 24" fill="none" stroke="#ef7b4f" stroke-width="1.6"><rect x="2" y="5" width="20" height="14" rx="2"/><path d="M2 10h20"/></svg>
  <div><h4>Secure Payment</h4><p>100% secure payment</p></div>
</div>
<div class="abs perk" style="left:458px">
  <svg width="14" height="14" viewBox="0 0 24 24" fill="none" stroke="#ef7b4f" stroke-width="1.6"><path d="M4 14v-2a8 8 0 0 1 16 0v2"/><rect x="2" y="13" width="4" height="6" rx="1"/><rect x="18" y="13" width="4" height="6" rx="1"/></svg>
  <div><h4>24/7 Support</h4><p>Dedicated support</p></div>
</div>
<div class="abs rule"></div>

<div class="abs tab active" style="left:248px">New Arrivals</div>
<div class="abs tab" style="left:322px">Feature Product</div>
<div class="abs tab" style="left:412px">Sale Item</div>

<div class="abs card" style="left:136px;top:374px"><div class="shot red" role="img" aria-label="Photo of two red shrimp"></div><div class="name">Product name</div><div class="price">$14.00<s>$35.00</s></div></div>
<div class="abs card" style="left:244px;top:374px"><div class="shot orange" role="img" aria-label="Photo of a cooked shrimp"></div><div class="name">Product name</div><div class="price">$14.00<s>$35.00</s></div></div>
<div class="abs card" style="left:353px;top:374px"><div class="shot brown" role="img" aria-label="Photo of a raw tiger shrimp"></div><div class="name">Product name</div><div class="price">$14.00<s>$35.00</s></div></div>
<div class="abs card" style="left:461px;top:374px"><div class="shot trio" role="img" aria-label="Photo of three red shrimp"></div><div class="name">Product name</div><div class="price">$14.00<s>$35.00</s></div></div>

<div class="abs card" style="left:136px;top:503px"><div class="shot brown" role="img" aria-label="Photo of a raw tiger shrimp"></div><div class="name">Product name</div><div class="price">$14.00<s>$35.00</s></div></div>
<div class="abs card" style="left:244px;top:503px"><div class="shot trio" role="img" aria-label="Photo of three red shrimp"></div><div class="name">Product name</div><div class="price">$14.00<s>$35.00</s></div></div>
<div class="abs card" style="left:353px;top:503px"><div class="shot red" role="img" aria-label="Photo of two red shrimp"></div><div class="name">Product name</div><div class="price">$14.00<s>$35.00</s></div></div>
<div class="abs card" style="left:461px;top:503px"><div class="shot orange" role="img" aria-label="Photo of a cooked shrimp"></div><div class="name">Product name</div><div class="price">$14.00<s>$35.00</s></div></div>

<div class="abs card" style="left:136px;top:632px"><div class="shot red" role="img" aria-label="Photo of two red shrimp"></div><div class="name">Product name</div><div class="price">$14.00<s>$35.00</s></div></div>
<div class="abs card" style="left:244px;top:632px"><div class="shot orange" role="img" aria-label="Photo of a cooked shrimp"></div><div class="name">Product name</div><div class="price">$14.00<s>$35.00</s></div></div>
<div class="abs card" style="left:353px;top:632px"><div class="shot brown" role="img" aria-label="Photo of a raw tiger shrimp"></div><div class="name">Product name</div><div class="price">$14.00<s>$35.00</s></div></div>
<div class="abs card" style="left:461px;top:632px"><div class="shot trio" role="img" aria-label="Photo of three red shrimp"></div><div class="name">Product name</div><div class="price">$14.00<s>$35.00</s></div></div>

<div class="abs hair" style="left:134px;width:170px"></div>
<div class="abs hair" style="left:388px;width:172px"></div>
<div class="abs btn-go">GO TO SHOP</div>

<section class="abs why" role="img" aria-label="Background photo of a pile of cooked shrimp"></section>
<div class="abs why-title">Why Choose Us</div>
<div class="abs why-line"></div>
<div class="abs why-ring"></div>
<div class="abs point left" style="left:169px;top:893px"><h5>Eat Healthier</h5><p>Modi tempora incidunt ut<br>labore dolore magnam ali-</p></div>
<div class="abs point left" style="left:169px;top:936px"><h5>We Have Brands</h5><p>Modi tempora incidunt ut<br>labore dolore magnam ali-</p></div>
<div class="abs point" style="left:409px;top:891px"><h5>Fresh And Clean Products</h5><p>Modi tempora incidunt ut<br>labore dolore magnam ali-</p></div>
<div class="abs point" style="left:409px;top:934px"><h5>Modern Process</h5><p>Modi tempora incidunt ut<br>labore dolore magnam ali-</p></div>

<section class="abs newsletter"></section>
<div class="abs nl-title">Subscribe to our Newsletter</div>
<div class="abs nl-sub">Subscribe to our newsletter and get 10% off your first purchase</div>
<div class="abs nl-input">Your email</div>
<div class="abs nl-btn">SUBSCRIBE</div>

<footer>
  <div class="abs pay" style="left:126px;background:#6b3fa0"></div>
  <div class="abs pay" style="left:144px;background:#e8e8e8"></div>
  <div class="abs pay" style="left:162px;background:#2f6fb5"></div>
  <div class="abs pay" style="left:180px;background:#dfe7f2"></div>
  <div class="abs pay" style="left:198px;background:#e8a14a"></div>
  <div class="abs pay" style="left:216px;background:#dfe4ef"></div>
  <div class="abs foot-brand"><div class="brand-dot"></div><div class="brand-name">Pelican Crest</div></div>
  <div class="abs social-dot" style="left:486px;top:1132px"></div>
  <div class="abs social-dot" style="left:508px;top:1132px"></div>
  <div class="abs social-dot" style="left:530px;top:1132px"></div>
  <div class="abs social-dot" style="left:552px;top:1132px"></div>
  <div class="abs copy">© Copyright 2019 pelicancrest.com</div>
  <div class="abs foot-links">
    <span style="left:0">About</span>
    <span style="left:27px">Blogs</span>
    <span style="left:52px">Privacy Policy</span>
    <span style="left:100px">Contact</span>
    <span style="left:132px">FAQs</span>
  </div>
</footer>

</body>
</html>
```